Brindle painting & waterproofing business card.

Business cards updated to reflect photos attached. we have given the photos of the old business cards and some of our updated designs for other items we have here in the office. Please see attached. if anyone needs to contact us directly for clarification you can email us at brindlerestoration@mailvane.com

Industry/Entity Type

Construction

Contact Information for Business Card

See attached photos

Font styles to use
Other font styles liked:
• Same as photos

Colors
ec1f27

Requirements
Must have
• Employee Names,
• Gordon Brindle II, Supervisor/Owner
• Gord Brindle, President/Owner
• Tim Harker, Sales Representative
• Lou Marsten, Supervisor
• Change 20 years to 25
Nice to have
• ideas reflecting the attached photos
Should not have
• should not be exactly like attached photos as those are old business card but reflect to match new logo listed as kelvar van and cup photo.

```html
<!DOCTYPE html>
<html lang="en">
<head>
<meta charset="utf-8">
<title>Brindle's Painting & Restoration – Business Card</title>
<link rel="stylesheet" href="https://fonts.googleapis.com/css2?family=Poppins:wght@400;500;600&family=Oswald:wght@500&display=swap">
<style>
  :root {
    --bg: #8a8a8a;
    --brand-orange: #dd4520;
    --brand-red: #e2401f;
    --card-white: #f7f7f7;
    --ink: #1e1e1e;
    --rule: #7a7a7a;
    --on-orange: #ffffff;
  }
  * { box-sizing: border-box; margin: 0; padding: 0; }
  html, body { width: 1200px; height: 960px; overflow: hidden; }
  body {
    background: var(--bg);
    font-family: "Poppins", sans-serif;
    display: flex;
    align-items: center;
    justify-content: center;
    gap: 40px;
  }
  .card {
    width: 560px;
    height: 320px;
    border-radius: 18px;
    position: relative;
    overflow: hidden;
    box-shadow: 0 8px 24px rgba(0,0,0,.25);
  }

  /* Back: orange services side */
  .card--back { background: var(--brand-orange); color: var(--on-orange); }
  .anniversary-mark {
    position: absolute; top: 26px; right: 30px;
    width: 78px; height: 50px;
    border-radius: 6px;
    background: rgba(255,255,255,.22);
  }
  .card--back .content {
    position: absolute; left: 0; right: 0; top: 82px;
    text-align: center;
  }
  .wordmark {
    font-family: "Poppins", sans-serif;
    font-weight: 600;
    letter-spacing: 1px;
    text-transform: uppercase;
    line-height: 1.1;
  }
  .card--back .wordmark { font-size: 30px; color: var(--on-orange); }
  .card--back .tagline {
    margin-top: 10px;
    font-size: 12.5px; font-weight: 600; text-transform: uppercase; line-height: 1.35;
  }
  .card--back .license { margin-top: 6px; font-size: 10.5px; }
  .card--back .services { margin-top: 14px; font-size: 14px; line-height: 1.45; }

  /* Front: white contact side */
  .card--front { background: var(--card-white); color: var(--ink); }
  .card--front .wordmark {
    position: absolute; left: 34px; top: 36px;
    font-size: 28px; color: var(--brand-red);
  }
  .contact {
    position: absolute; right: 34px; top: 118px; width: 250px;
    font-size: 12.5px; line-height: 1.6; text-transform: uppercase;
    border-bottom: 1px solid var(--rule); padding-bottom: 6px;
  }
  .person {
    position: absolute; left: 34px; right: 34px; bottom: 30px;
  }
  .person__name {
    font-family: "Oswald", sans-serif; font-weight: 500;
    font-size: 30px; color: var(--brand-red); text-transform: uppercase; line-height: 1.1;
  }
  .person__role { font-size: 12px; font-weight: 500; text-transform: uppercase; }
  .person__web { font-size: 13px; text-transform: uppercase; margin-top: 2px; padding-bottom: 8px; border-bottom: 1px solid var(--rule); }
  .person__address { font-size: 14.5px; text-transform: uppercase; margin-top: 8px; }
</style>
</head>
<body>
  <section class="card card--back" aria-label="Card back">
    <div class="anniversary-mark" role="img" aria-label="25 years anniversary mark"></div>
    <div class="content">
      <div class="wordmark">Brindle's Painting<br>&amp; Restoration</div>
      <p class="tagline">Waterproofing &amp; Concrete Restoration<br>Specializing in Hi-Rises &amp; Commercial</p>
      <p class="license">General Contractor &nbsp;CGC#4820916 &nbsp;Licensed &amp; Insured</p>
      <p class="services">
        Concrete Restoration • Waterproofing • Painting<br>
        Electrostatic • Expansion joints • Caulking<br>
        Deck Coating • Balustrades &amp; Railing
      </p>
    </div>
  </section>

  <section class="card card--front" aria-label="Card front">
    <div class="wordmark">Brindle's<br>Painting &amp;<br>Restoration</div>
    <div class="contact">
      <p>Phone : 555.786.2140</p>
      <p>Mobile : 555.553.8716</p>
      <p>brindlerestoration@mailvane.com</p>
    </div>
    <div class="person">
      <p class="person__name">Gordon Brindle II</p>
      <p class="person__role">Supervisor / Owner</p>
      <p class="person__web">www.brindlerestoration.com</p>
      <p class="person__address">240 Harbor Way &nbsp;Seabrook, FL 33990</p>
    </div>
  </section>
</body>
</html>
```